Marrowby's Vacation Rentals Business Card

Multi Million dollar villa rentals in the Dominican Republic.

Industry/Entity Type

Business

Contact Information for Business Card

I am looking for a high-end look around my company name/logo (see attached) on one side incorporating the following info: first and last name, title, address, phone #, email and company website. On the backside I want to add a full color picture of one of our villas (see attached).

```html
<!DOCTYPE html>
<html lang="en">
<head>
<meta charset="utf-8">
<title>Marrowby's Vacation Rentals – Business Card</title>
<link rel="stylesheet" href="https://fonts.googleapis.com/css2?family=Oswald:wght@500;700&family=Open+Sans:wght@400;600&display=swap">
<style>
  :root {
    --bg: #e6e6e1;
    --white: #ffffff;
    --ink: #1c1c1c;
    --orange-deep: #ea5a22;
    --orange-mid: #f07a22;
    --orange-light: #f39a2c;
    --sky: #8cc4ec;
    --pool: #2f9fd8;
    --pool-deep: #1672b8;
    --villa: #d9d4c8;
  }
  html, body {
    margin: 0;
    width: 1200px;
    height: 1200px;
    overflow: hidden;
    background: var(--bg);
  }
  .canvas {
    width: 1200px;
    height: 1200px;
    display: flex;
    flex-direction: column;
    align-items: center;
    justify-content: center;
    gap: 44px;
  }
  .card {
    position: relative;
    width: 900px;
    height: 514px;
    overflow: hidden;
    background: var(--white);
    box-shadow: 0 10px 28px rgba(0,0,0,0.16);
  }
  .card-art {
    position: absolute;
    inset: 0;
    width: 100%;
    height: 100%;
  }
  .brand {
    position: absolute;
    display: flex;
    align-items: center;
    gap: 12px;
  }
  .brand-dot {
    width: 26px;
    height: 26px;
    border-radius: 50%;
    background: var(--orange-mid);
    flex: none;
  }
  .brand-name {
    font-family: "Open Sans", sans-serif;
    font-weight: 600;
    color: var(--ink);
    font-size: 26px;
    line-height: 1.1;
    letter-spacing: 0.5px;
  }
  .brand-name small {
    display: block;
    font-size: 15px;
    letter-spacing: 2.5px;
    text-transform: uppercase;
  }
  .brand--front { left: 585px; top: 140px; }
  .brand--back { left: 560px; top: 195px; }

  .person {
    position: absolute;
    left: 70px;
    top: 150px;
    color: var(--white);
  }
  .person-name {
    font-family: "Oswald", sans-serif;
    font-weight: 700;
    font-size: 58px;
    line-height: 1;
    text-transform: uppercase;
    margin: 0;
  }
  .person-title {
    font-family: "Oswald", sans-serif;
    font-weight: 500;
    font-size: 21px;
    text-transform: uppercase;
    margin: 8px 0 10px;
  }
  .address, .contact {
    font-family: "Open Sans", sans-serif;
    font-size: 17px;
    line-height: 1.45;
    margin: 0;
    color: var(--white);
  }
  .contact {
    position: absolute;
    left: 70px;
    bottom: 52px;
  }
</style>
</head>
<body>
<main class="canvas">

  <section class="card card--front" aria-label="Business card, photo side">
    <svg class="card-art" viewBox="0 0 900 514" preserveAspectRatio="none">
      <defs>
        <linearGradient id="villaPhoto" x1="0" y1="0" x2="0" y2="1">
          <stop offset="0" stop-color="var(--sky)"/>
          <stop offset="0.38" stop-color="var(--villa)"/>
          <stop offset="0.55" stop-color="var(--pool)"/>
          <stop offset="1" stop-color="var(--pool-deep)"/>
        </linearGradient>
      </defs>
      <rect width="900" height="514" fill="url(#villaPhoto)" role="img" aria-label="Photograph of a white villa with terracotta roof, palm trees and a blue swimming pool"/>
      <path class="brand-panel" fill="var(--white)"
        d="M 500 0 L 820 0 C 880 70 850 190 780 250 C 710 310 640 330 610 430 C 570 340 480 300 470 200 C 462 110 480 50 500 0 Z"/>
    </svg>
    <div class="brand brand--front">
      <span class="brand-dot"></span>
      <span class="brand-name">Marrowby's<small>Vacation Rentals</small></span>
    </div>
  </section>

  <section class="card card--back" aria-label="Business card, contact side">
    <svg class="card-art" viewBox="0 0 900 514" preserveAspectRatio="none">
      <rect width="900" height="514" fill="var(--white)"/>
      <path class="band-light" fill="var(--orange-light)"
        d="M 430 0 L 560 0 C 500 90 470 180 520 270 C 560 340 640 420 720 514 L 450 514 C 420 400 380 300 400 180 C 410 110 420 50 430 0 Z"/>
      <path class="band-deep" fill="var(--orange-deep)"
        d="M 0 0 L 440 0 C 470 80 460 170 430 260 C 400 350 420 440 470 514 L 0 514 Z"/>
      <path class="swoosh-top" fill="none" stroke="var(--orange-mid)" stroke-width="22" stroke-linecap="round"
        d="M 540 110 C 600 30 720 10 840 20"/>
      <path class="swoosh-wave" fill="none" stroke="var(--orange-mid)" stroke-width="26" stroke-linecap="round"
        d="M 560 330 C 620 420 700 420 760 360 C 820 300 860 260 900 250"/>
    </svg>

    <div class="person">
      <h1 class="person-name">Elias Wren</h1>
      <p class="person-title">Graphic Design</p>
      <p class="address">Your Street address text here<br>City with post code, Country</p>
    </div>

    <p class="contact">+392 55 418 07<br>hello@marrowbysrentals.com<br>www.marrowbysrentals.com</p>

    <div class="brand brand--back">
      <span class="brand-dot"></span>
      <span class="brand-name">Marrowby's<small>Vacation Rentals</small></span>
    </div>
  </section>

</main>
</body>
</html>
```